Letterhead Design Project

I need letterhead designed for my law firm. It would also be used for web based stuff as well.

Industry/Entity Type

Law Firm

```html
<!DOCTYPE html>
<html lang="en">
<head>
<meta charset="utf-8">
<title>Harlow &amp; Mercer Letterhead</title>
<link rel="stylesheet" href="https://fonts.googleapis.com/css2?family=Montserrat:wght@500;600&family=Open+Sans:wght@400;700&display=swap">
<style>
  :root {
    --backdrop: #d2d3d5;
    --paper: #ffffff;
    --ink-dark: #22363a;
    --accent-orange: #e07000;
    --accent-blue: #1a93c0;
    --name-grey: #3d3d3d;
    --white: #ffffff;
  }
  * { margin: 0; padding: 0; box-sizing: border-box; }
  html, body {
    width: 1200px;
    height: 1000px;
    overflow: hidden;
    background: var(--backdrop);
  }
  .letterhead {
    position: absolute;
    left: 294px;
    top: 104px;
    width: 612px;
    height: 791px;
    background: var(--paper);
  }
  .top-band {
    position: absolute;
    left: 0; top: 0;
    width: 100%;
    height: 17px;
    background: var(--ink-dark);
  }
  .top-band__accent {
    position: absolute;
    left: 0; top: 0;
    width: 64px;
    height: 100%;
    background: var(--accent-orange);
  }
  .brand {
    position: absolute;
    left: 64px;
    top: 46px;
    display: flex;
    align-items: flex-start;
    gap: 17px;
  }
  .brand__mark {
    width: 32px;
    height: 34px;
    border-radius: 50%;
    background: var(--accent-blue);
    margin-top: 1px;
  }
  .brand__name {
    font-family: "Montserrat", sans-serif;
    font-weight: 600;
    font-size: 21px;
    font-variant: small-caps;
    letter-spacing: 0.2px;
    line-height: 24px;
    color: var(--name-grey);
  }
  .brand__tagline {
    font-family: "Montserrat", sans-serif;
    font-weight: 500;
    font-size: 11px;
    color: var(--name-grey);
    margin-top: 1px;
  }
  .footer-band {
    position: absolute;
    left: 0;
    top: 714px;
    width: 100%;
    height: 77px;
    background: var(--ink-dark);
  }
  .footer-band__accent {
    position: absolute;
    left: 0; top: 0;
    width: 9px;
    height: 100%;
    background: var(--accent-orange);
  }
  .contact {
    position: absolute;
    top: 20px;
    font-family: "Open Sans", sans-serif;
    font-size: 9px;
    line-height: 11px;
    color: var(--white);
  }
  .contact__label {
    font-weight: 700;
    color: var(--accent-orange);
    margin-bottom: 2px;
  }
  .contact--address { left: 65px; }
  .contact--phone { left: 180px; }
  .contact--web { left: 296px; }
</style>
</head>
<body>
  <main class="letterhead">
    <div class="top-band"><div class="top-band__accent"></div></div>

    <header class="brand">
      <div class="brand__mark"></div>
      <div class="brand__text">
        <div class="brand__name">Harlow &amp; Mercer</div>
        <div class="brand__tagline">Attorneys of Law</div>
      </div>
    </header>

    <footer class="footer-band">
      <div class="footer-band__accent"></div>
      <div class="contact contact--address">
        <div class="contact__label">Address</div>
        <div>1280 Linden Avenue NW</div>
        <div>Washington, DC 20005</div>
      </div>
      <div class="contact contact--phone">
        <div class="contact__label">Phone</div>
        <div>(202) 555-0148</div>
        <div>Toll Free: 855-555-0172</div>
      </div>
      <div class="contact contact--web">
        <div class="contact__label">Contact web</div>
        <div>www.harlowmercer.com</div>
        <div>Nina@harlowmercer.com</div>
      </div>
    </footer>
  </main>
</body>
</html>
```